Saffron Lantern Court Business Card

I am looking for a business card desgined for my restaurant. It is an Indian restaurant, we are looking for something thats modern, yet traditional with the indian culture, we are looking for colors that match our logo. The logo is a design of the building with the name of the restaurant. for more information on the restaurant go to www.saffronlanterncourt.example

Industry/Entity Type

Indian Restaurant

Contact Information for Business Card

we are looking for somthing thats modern, yet traditional with the indian culture, we are looking for colors that match our logo. The logo is a design of the building with the name of the restaurant. for more information on the restaurant go to www.saffronlanterncourt.example

Requirements
Must have
• The logo that is attached,
• Name: Harvinder Oberoi,
• address of the restaurant: 7328 West Larkspur Rd, Phoenix, Arizona, 85213
• Phone: (602) 555-0147
• Fax: (602) 555-0193
• Restaurant Catering Banquet
• Website: www.SaffronLanternCourt.example
Nice to have
• wanted to get something that goes with the theme of the restaurant, which is traditional but also keep a very professional and modern touch

```html
<!DOCTYPE html>
<html lang="en">
<head>
<meta charset="utf-8">
<title>Saffron Lantern Court Business Card</title>
<link href="https://fonts.googleapis.com/css2?family=Lato:wght@400;700&display=swap" rel="stylesheet">
<style>
  :root {
    --backdrop: #3b3b3b;
    --card: #2a2a2b;
    --card-edge: #323233;
    --brand-red: #d9482c;
    --accent-orange: #f07a2a;
    --text-light: #d9d9d9;
  }
  * { margin: 0; padding: 0; box-sizing: border-box; }
  html, body { width: 1200px; height: 1000px; overflow: hidden; }
  body {
    background: var(--backdrop);
    font-family: "Lato", Arial, sans-serif;
    position: relative;
  }
  .card {
    position: absolute;
    left: 288px;
    width: 625px;
    height: 357px;
    background: linear-gradient(135deg, var(--card-edge), var(--card) 60%);
    box-shadow: 0 6px 18px rgba(0,0,0,0.45);
  }
  .card-front { top: 141px; }
  .card-back { top: 532px; }

  .brand-name {
    position: absolute;
    color: var(--brand-red);
    font-weight: 700;
    text-transform: uppercase;
    text-align: center;
    line-height: 1.08;
    letter-spacing: 2px;
  }
  .since {
    position: absolute;
    color: var(--brand-red);
    font-size: 11px;
    letter-spacing: 3px;
    text-align: center;
  }
  .card-front .brand-name { left: 0; width: 625px; top: 100px; font-size: 48px; }
  .card-front .since { left: 0; width: 625px; top: 305px; }

  .card-back .brand-name { left: 50px; width: 260px; top: 100px; font-size: 44px; }
  .card-back .since { left: 50px; width: 260px; top: 296px; }

  .divider { position: absolute; left: 309px; }

  .contact {
    position: absolute;
    left: 335px;
    top: 126px;
    color: var(--text-light);
    font-size: 14px;
    line-height: 18px;
  }
  .contact .person-name { color: var(--accent-orange); font-weight: 700; font-size: 17px; line-height: 20px; }
  .contact .person-role { margin-bottom: 12px; }
  .contact .address { margin-bottom: 11px; }
  .contact .line { display: flex; align-items: center; gap: 6px; line-height: 20px; }
  .contact svg { width: 11px; height: 11px; flex: none; }
</style>
</head>
<body>
  <section class="card card-front">
    <div class="brand-name">Saffron<br>Lantern<br>Court</div>
    <div class="since">SINCE 1985</div>
  </section>

  <section class="card card-back">
    <div class="brand-name">Saffron<br>Lantern<br>Court</div>
    <div class="since">SINCE 1985</div>

    <svg class="divider" width="2" height="150" style="top:128px" aria-hidden="true">
      <rect x="0" y="0" width="2" height="34" fill="var(--brand-red)"/>
      <rect x="0" y="52" width="2" height="98" fill="var(--accent-orange)"/>
    </svg>

    <div class="contact">
      <div class="person-name">Harvinder Oberoi</div>
      <div class="person-role">Founder &amp; CEO</div>
      <div class="address">7328 West Larkspur Rd,<br>Phoenix, Arizona, 85213</div>
      <div class="line">
        <svg viewBox="0 0 12 12" aria-label="Phone"><path d="M2 1 L4.5 1 L5 3.5 L3.8 4.5 Q5 7 7.5 8.2 L8.5 7 L11 7.5 L11 10 Q6 11 2.5 7 Q0.5 4 2 1Z" fill="var(--accent-orange)"/></svg>
        <span>(602) 555-0147</span>
      </div>
      <div class="line">
        <svg viewBox="0 0 12 12" aria-label="Fax"><rect x="3" y="1" width="6" height="3" fill="var(--accent-orange)"/><rect x="1" y="4.5" width="10" height="5" rx="1" fill="var(--accent-orange)"/><rect x="3" y="8" width="6" height="3" fill="var(--accent-orange)"/></svg>
        <span>(602) 555-0193</span>
      </div>
      <div class="line">
        <svg viewBox="0 0 12 12" aria-label="Website"><circle cx="6" cy="6" r="5" fill="var(--accent-orange)"/><path d="M1 6 H11 M6 1 Q3 6 6 11 M6 1 Q9 6 6 11" stroke="var(--card)" stroke-width="0.8" fill="none"/></svg>
        <span>www.SaffronLanternCourt.example</span>
      </div>
    </div>
  </section>
</body>
</html>
```